Website redesign

Looking to redesign our existing website. (quill7meadows.com.au)
New design needs to be bright, fun and have an easy flowing.
The website needs to be design with call to action.

Some examples of other websites:
fernquaylo.com
tovanmilk.com.au

We are happy with the content of our existing website.

Target Market(s)

other businesses

Industry/Entity Type

Business Service

Number of Pages Required

5+ page

Requirements
Must have
• Theme redesign
Cool animation similar to fernquaylo.com

```html
<!DOCTYPE html>
<html lang="en">
<head>
<meta charset="utf-8">
<title>Quill 7 Meadows — Virtual Assistants</title>
<link href="https://fonts.googleapis.com/css2?family=Source+Sans+3:wght@300;400;600;700&display=swap" rel="stylesheet">
<style>
:root{
  --blue:#13a6e0;
  --blue-dark:#0e9bd6;
  --ink:#2a2f3a;
  --muted:#8a8f98;
  --hero-bg:#f4f6f9;
  --band-bg:#eef3fa;
  --white:#ffffff;
  --line:#cfd6df;
}
*{box-sizing:border-box;margin:0;padding:0}
html,body{width:1200px;height:3647px;overflow:hidden}
body{position:relative;font-family:"Source Sans 3",sans-serif;color:var(--ink);background:var(--white)}
.abs{position:absolute}
.center{text-align:center}

/* header */
.site-header{top:0;left:0;width:1200px;height:110px;background:var(--white);box-shadow:0 2px 6px rgba(0,0,0,.08);z-index:2}
.brand{left:66px;top:40px;display:flex;align-items:center;gap:10px;font-size:22px;font-weight:600;color:var(--ink);letter-spacing:.5px}
.brand-dot{width:14px;height:14px;border-radius:50%;background:var(--blue)}
.nav{right:66px;top:43px;height:67px;display:flex;gap:54px;font-size:16px}
.nav a{color:var(--ink);text-decoration:none;position:relative;height:67px}
.nav a.active::after{content:"";position:absolute;left:0;right:0;bottom:0;height:3px;background:var(--blue)}

/* hero */
.hero{top:110px;left:0;width:1200px;height:746px;background:var(--hero-bg)}
.hero-title{left:40px;width:456px;top:186px;font-size:31px;font-weight:400;line-height:48px;text-transform:uppercase}
.hero-title strong{color:var(--blue);font-weight:700}
.hero-sub{left:40px;width:456px;top:294px;font-size:18px}
.btn{display:flex;align-items:center;justify-content:center;font-size:14px;border-radius:2px}
.btn-solid{background:var(--blue);color:var(--white)}
.btn-ghost{border:2px solid var(--blue);color:var(--blue);background:var(--white)}
.hero-video{left:617px;top:191px;width:444px;height:272px;border-radius:16px;border:3px solid var(--white);
  background:linear-gradient(120deg,#c9c3c2 0%,#9fb4c6 45%,#7fb8df 100%);box-shadow:0 4px 14px rgba(0,0,0,.15)}
.play{left:813px;top:304px}

.intro-card{left:222px;top:552px;width:756px;height:255px;background:var(--white);box-shadow:0 2px 12px rgba(0,0,0,.08)}
.intro-card h2{position:absolute;top:32px;width:100%;font-size:15px;font-weight:600}
.intro-card p{position:absolute;top:80px;left:110px;width:536px;font-size:12px;line-height:24px;color:#555}

/* process */
.process{top:856px;left:0;width:1200px;height:1194px;background:var(--band-bg)}
.section-title{font-size:30px;font-weight:300;letter-spacing:1px;width:1200px;left:0}
.section-title strong{font-weight:700}
.step-num{width:44px;height:44px;border-radius:50%;background:var(--blue);color:var(--white);font-size:19px;display:flex;align-items:center;justify-content:center}
.step{width:328px}
.step h3{font-size:15px;font-weight:600;color:var(--ink);line-height:24px}
.step p{font-size:15.5px;font-weight:300;line-height:24px;color:#7d838c}
.photo{box-shadow:0 3px 10px rgba(0,0,0,.2)}
.photo-meeting{left:712px;top:1019px;width:488px;height:363px;background:linear-gradient(135deg,#8fb0bb,#4c8fb0 60%,#2f6f95)}
.photo-desk{left:0;top:1575px;width:483px;height:362px;background:linear-gradient(135deg,#3b6f86,#6fa9c4 55%,#b6d6e6)}

/* services */
.services-intro{left:0;width:1200px;top:2159px;font-size:12px}
.services-intro strong{display:block;margin-top:8px;color:var(--blue);font-size:14px;font-weight:700;letter-spacing:.5px}
.service-card{top:2284px;width:214px;height:239px;background:var(--white);box-shadow:0 2px 10px rgba(0,0,0,.12);display:flex;flex-direction:column;align-items:center;justify-content:center}
.service-card h4{color:var(--blue);font-size:15px;font-weight:700;line-height:24px;text-align:center;margin-top:12px}
.service-card span{font-size:11px;color:#555;margin-top:4px}
.simple-line{left:0;width:1200px;top:2590px;font-size:21px;font-weight:300;line-height:25px;color:#555}
.simple-line strong{color:var(--blue);font-weight:700}

/* quote */
.quote{top:2691px;left:0;width:1200px;height:759px;background:var(--band-bg)}
.quote-sub{left:0;width:1200px;top:2807px;font-size:17px;color:var(--muted);font-weight:300}
.why-title{left:80px;width:434px;top:2902px;font-size:28px;font-weight:600}
.why-title strong{color:var(--blue)}
.why-sub{left:80px;width:434px;top:2962px;font-size:17px}
.checks{left:154px;top:3034px;list-style:none}
.checks li{display:flex;align-items:center;gap:26px;height:48px;font-size:15px;font-weight:600;letter-spacing:.4px}
.field{background:var(--white);border:1px solid var(--line);font-size:12px;color:var(--muted);padding:0 11px;display:flex;align-items:center}
.field.tall{align-items:flex-start;padding-top:10px}
.captcha{left:811px;top:3249px;width:178px;height:41px;background:#222;border-radius:3px;display:flex;align-items:center;gap:8px;padding-left:8px;color:var(--white);font-size:9px}
.captcha i{width:16px;height:16px;background:var(--white);border-radius:2px}
.subscribe{left:800px;top:3318px;font-size:13px;display:flex;align-items:center;gap:16px}
.subscribe i{width:9px;height:9px;border:2px solid var(--ink);border-radius:50%}
.city{left:521px;top:3407px;width:162px;height:43px;background:linear-gradient(180deg,#7fcdef,#3db4e6)}

/* footer */
.site-footer{top:3450px;left:0;width:1200px;height:197px;background:var(--blue);color:var(--white);text-align:center}
.footer-brand{margin-top:58px;font-size:24px;font-weight:600;letter-spacing:1px;display:flex;justify-content:center;align-items:center;gap:10px}
.footer-brand i{width:14px;height:14px;border-radius:50%;background:var(--white)}
.footer-tag{margin-top:36px;font-size:12px}
.footer-copy{margin-top:12px;font-size:9px}
</style>
</head>
<body>

<header class="site-header abs">
  <div class="brand abs"><span class="brand-dot"></span>QUILL 7 MEADOWS</div>
  <nav class="nav abs">
    <a class="active" href="#">Home</a><a href="#">Our Story</a><a href="#">Tips &amp; Tricks</a><a href="#">Contact Us</a><a href="#">FAQ</a>
  </nav>
</header>

<section class="hero abs"></section>
<h1 class="hero-title abs center">Virtual Assistant? <strong>More<br>like valuable asset!</strong></h1>
<p class="hero-sub abs center">Tech nerds on standby for setup, support and comms!</p>
<a class="btn btn-solid abs" style="left:75px;top:359px;width:181px;height:44px">Call Now</a>
<a class="btn btn-ghost abs" style="left:279px;top:359px;width:181px;height:44px">Get a Quote</a>
<svg class="abs" style="left:533px;top:138px" width="60" height="66" viewBox="0 0 60 66"><path d="M4 4 L52 52 M52 52 L52 30 M52 52 L30 52" stroke="#a9d8ef" stroke-width="6" fill="none"/></svg>
<svg class="abs" style="left:1098px;top:435px" width="70" height="56" viewBox="0 0 70 56"><path d="M66 52 L10 10 M10 10 L34 10 M10 10 L16 32" stroke="#a9d8ef" stroke-width="6" fill="none"/></svg>
<div class="hero-video abs" role="img" aria-label="Blurred video still of two people in an office"></div>
<svg class="play abs" width="46" height="46" viewBox="0 0 46 46"><circle cx="23" cy="23" r="23" fill="#fff"/><path d="M18 13 L33 23 L18 33Z" fill="#9fb4c6"/></svg>

<div class="intro-card abs center">
  <h2>Outsourcing. A big word that means big things for your business.</h2>
  <p>Virtual Assistants are the superheroes of the modern office. They can do everything your team can do on a computer at a fraction of the price! (Well, maybe not high five you when you've had a win, but a virtual high five is definitely on the table!)</p>
  <a class="btn btn-ghost abs" style="left:287px;top:178px;width:181px;height:45px">Get a Quote</a>
</div>

<section class="process abs"></section>
<h2 class="section-title abs center" style="top:886px">THE PROCESS</h2>

<div class="step-num abs" style="left:204px;top:961px">1</div>
<div class="step abs" style="left:274px;top:972px"><h3>Provide Your Preferred Qualifications.</h3><p>Set up a call with our team to specify the requirements and qualifications you're searching for in a Virtual Assistant. This will be our checklist for your perfect assistant! From there, we'll take care of shortlisting, testing, background checking and recruiting.</p></div>
<div class="step-num abs" style="left:204px;top:1152px">2</div>
<div class="step abs" style="left:274px;top:1163px"><h3>Endorsing the Shortlisted Candidates</h3><p>After the thorough vetting process, we'll put forward the best candidate. You can then conduct the final interview on your preferred communication platform at a time that suits you. Once the schedule is set, we'll let the candidates know!</p></div>
<div class="step-num abs" style="left:204px;top:1369px">3</div>
<div class="step abs" style="left:274px;top:1380px"><h3>Conducting the Final Interview</h3><p>The final interview is the perfect time to get to know the candidates. It'll help to have a list of questions prepared that will help you pick out the chosen one!</p></div>
<div class="photo photo-meeting abs" role="img" aria-label="Photo of two women talking at a desk with a laptop"></div>
<div class="photo photo-desk abs" role="img" aria-label="Photo of a virtual assistant working at two monitors"></div>
<div class="step-num abs" style="left:642px;top:1537px">4</div>
<div class="step abs" style="left:712px;top:1548px"><h3>Setting up the Tools</h3><p>Once you've chosen your Virtual Assistant, it's time for their system to be set up. You can get your own IT team onto the installation, otherwise, we've got a super team of tech peeps who can do it for you.</p></div>
<div class="step-num abs" style="left:642px;top:1706px">5</div>
<div class="step abs" style="left:712px;top:1717px"><h3>Your Magical Journey Begins</h3><p>Now you and your Virtual Assistant are all set up and ready to rumble! Feel the magic of having a reliable assistant to take on all the menial, repetitive, time-consuming tasks, and focus your energy on more important things. Meet new clients, explore business opportunities, or just spend some time with friends and family!</p></div>
<a class="btn btn-ghost abs" style="left:749px;top:1954px;width:181px;height:44px">Get a Quote</a>

<h2 class="section-title abs center" style="top:2098px;font-size:28px">OUR <strong>SERVICES</strong></h2>
<p class="services-intro abs center">We'll help you save tens (or even hundreds!) of thousands of dollars per year. But what do WE actually do?<strong>GLAD YOU ASKED!</strong></p>

<div class="service-card abs" style="left:66px">
  <svg width="66" height="80" viewBox="0 0 66 80"><circle cx="33" cy="40" r="32" fill="var(--blue)"/><rect x="6" y="28" width="54" height="16" rx="6" fill="#fff"/></svg>
</div>
<div class="service-card abs" style="left:351px">
  <svg width="66" height="80" viewBox="0 0 66 80"><circle cx="33" cy="36" r="24" fill="var(--blue)"/><path d="M6 40 A27 27 0 0 1 60 40" stroke="var(--blue)" stroke-width="5" fill="none"/><rect x="2" y="36" width="10" height="18" rx="4" fill="var(--blue)"/><path d="M8 54 Q14 70 34 68" stroke="var(--blue)" stroke-width="4" fill="none"/><circle cx="36" cy="68" r="4" fill="var(--blue)"/></svg>
</div>
<div class="service-card abs" style="left:635px">
  <svg width="34" height="34" viewBox="0 0 34 34"><rect x="2" y="2" width="30" height="30" fill="none" stroke="#555" stroke-width="2"/><rect x="7" y="7" width="7" height="20" fill="none" stroke="#555" stroke-width="2"/><g fill="#555"><rect x="18" y="8" width="10" height="4"/><rect x="18" y="15" width="3" height="3"/><rect x="23" y="15" width="3" height="3"/><rect x="18" y="20" width="3" height="3"/><rect x="23" y="20" width="3" height="3"/></g></svg>
  <h4>SET UP THE PHONE<br>SYSTEM</h4>
  <span>(Their Own Bat Phone!)</span>
</div>
<div class="service-card abs" style="left:920px">
  <svg width="64" height="96" viewBox="0 0 64 96"><path d="M12 4 H52 V40 A20 20 0 0 1 12 40Z" fill="var(--blue)"/><path d="M12 12 H2 V24 Q2 36 14 38 M52 12 H62 V24 Q62 36 50 38" stroke="var(--blue)" stroke-width="4" fill="none"/><path d="M32 14 L35 23 L44 23 L37 28 L40 37 L32 31 L24 37 L27 28 L20 23 L29 23Z" fill="#fff"/><rect x="27" y="58" width="10" height="16" fill="var(--blue)"/><rect x="14" y="74" width="36" height="16" fill="var(--blue)"/><rect x="6" y="90" width="52" height="4" fill="var(--blue)"/></svg>
</div>

<p class="simple-line abs center">See? <strong>It's that simple!</strong> The only thing to do now is to finally<br>get started on the quote... just scroll down a little more.</p>

<section class="quote abs"></section>
<svg class="abs" style="left:846px;top:2649px" width="64" height="104" viewBox="0 0 64 104"><path d="M20 2 H44 V62 H60 L32 100 L4 62 H20Z" fill="#bfe6f7" stroke="var(--blue)" stroke-width="3"/></svg>
<h2 class="section-title abs center" style="top:2746px;font-size:30px">GET A <strong>QUOTE</strong></h2>
<p class="quote-sub abs center">Fill in the form below to get a Quote for your own personal Virtual Assistant</p>

<h3 class="why-title abs center">WHY CHOOSE <strong>OUR TEAM</strong></h3>
<p class="why-sub abs center">Why are we your new best outsourcing friend?</p>
<ul class="checks abs">
  <li><svg width="28" height="28" viewBox="0 0 28 28"><circle cx="14" cy="14" r="12" fill="none" stroke="var(--blue)" stroke-width="2.5"/><path d="M8 14 L12.5 18.5 L20 10" stroke="var(--blue)" stroke-width="2.5" fill="none"/></svg>Your Own Virtual Assistant</li>
  <li><svg width="28" height="28" viewBox="0 0 28 28"><circle cx="14" cy="14" r="12" fill="none" stroke="var(--blue)" stroke-width="2.5"/><path d="M8 14 L12.5 18.5 L20 10" stroke="var(--blue)" stroke-width="2.5" fill="none"/></svg>One Invoice Per Month</li>
  <li><svg width="28" height="28" viewBox="0 0 28 28"><circle cx="14" cy="14" r="12" fill="none" stroke="var(--blue)" stroke-width="2.5"/><path d="M8 14 L12.5 18.5 L20 10" stroke="var(--blue)" stroke-width="2.5" fill="none"/></svg>No Super or TAX</li>
  <li><svg width="28" height="28" viewBox="0 0 28 28"><circle cx="14" cy="14" r="12" fill="none" stroke="var(--blue)" stroke-width="2.5"/><path d="M8 14 L12.5 18.5 L20 10" stroke="var(--blue)" stroke-width="2.5" fill="none"/></svg>Dedicated To Your Business Only</li>
  <li><svg width="28" height="28" viewBox="0 0 28 28"><circle cx="14" cy="14" r="12" fill="none" stroke="var(--blue)" stroke-width="2.5"/><path d="M8 14 L12.5 18.5 L20 10" stroke="var(--blue)" stroke-width="2.5" fill="none"/></svg>Dedicated Phone System</li>
  <li><svg width="28" height="28" viewBox="0 0 28 28"><circle cx="14" cy="14" r="12" fill="none" stroke="var(--blue)" stroke-width="2.5"/><path d="M8 14 L12.5 18.5 L20 10" stroke="var(--blue)" stroke-width="2.5" fill="none"/></svg>IT Setup and Support</li>
</ul>

<div class="field abs" style="left:654px;top:2922px;width:225px;height:31px">Your First Name</div>
<div class="field abs" style="left:907px;top:2922px;width:225px;height:31px">Your Surname</div>
<div class="field abs" style="left:654px;top:2977px;width:478px;height:31px">Business Name</div>
<div class="field abs" style="left:654px;top:3032px;width:225px;height:31px">Contact Number</div>
<div class="field abs" style="left:907px;top:3032px;width:225px;height:31px">Email</div>
<div class="field tall abs" style="left:654px;top:3097px;width:478px;height:118px">Describe the tasks you'll need from your Virtual Assistant</div>
<div class="captcha abs"><i></i>I'm not a robot</div>
<div class="subscribe abs"><i></i>Subscribe to our newsletter</div>
<a class="btn btn-solid abs" style="left:846px;top:3369px;width:94px;height:31px;font-size:13px">Submit</a>
<div class="city abs" role="img" aria-label="Illustration of a row of city buildings"></div>

<footer class="site-footer abs">
  <div class="footer-brand"><i></i>QUILL 7 MEADOWS</div>
  <p class="footer-tag">Virtual Assistant? More Like Valuable Asset!</p>
  <p class="footer-copy">© 2020 QUILL 7 MEADOWS | All rights reserved.</p>
</footer>

</body>
</html>
```